Estate Agent A5 Doublesided leaflet

We would like to have a very vibrant, simple, elegant and memorable leaflet promoting our sales division launch and the special offer of only 0.5% fee for instructions received in March 2015

Target Market(s)

Our customers usually have properties valued 500,000USD or more

Industry/Entity Type

Sales

Requirements
Must have
• originality, easy to remember, clear message to client
Something unique, as in the leaflet attached below

```html
<!DOCTYPE html>
<html lang="en">
<head>
<meta charset="utf-8">
<title>Oakridge Sales &amp; Lettings – Leaflet</title>
<link rel="stylesheet" href="https://fonts.googleapis.com/css2?family=Inter:wght@300;400;600;700&display=swap">
<style>
  :root {
    --brand-dark: #1e5b2d;
    --brand-bright: #2f9a3c;
    --map-light: #dfe9cf;
    --map-mid: #c9dbb3;
    --footer-green: #4c6a4b;
    --ink: #1a1a1a;
    --paper: #ffffff;
    --tone-green: #b6d27a;
    --tone-yellow: #f4cf4a;
    --tone-orange: #ef9a2e;
    --tone-red: #c8403a;
  }
  * { box-sizing: border-box; margin: 0; padding: 0; }
  html, body { width: 847px; height: 1200px; overflow: hidden; background: var(--paper); }
  body { font-family: "Inter", Arial, sans-serif; color: var(--ink); }

  .leaflet { position: relative; width: 847px; height: 1200px; background: var(--paper); }

  .region-map {
    position: absolute; left: 0; top: 0; width: 847px; height: 302px;
    background: linear-gradient(160deg, var(--map-light) 0%, var(--map-mid) 60%, #bcd3a3 100%);
  }

  .brand { position: absolute; left: 54px; top: 151px; }
  .brand-row { display: flex; align-items: center; gap: 12px; }
  .brand-square { width: 111px; height: 111px; background: var(--brand-dark); }
  .brand-name {
    font-weight: 700; font-size: 80px; line-height: 1; color: var(--brand-dark);
    letter-spacing: -2px;
  }
  .brand-tagline {
    display: block; margin-top: 2px; margin-left: 123px;
    font-weight: 600; font-size: 19px; color: var(--brand-dark); letter-spacing: 0.5px;
  }

  .resources {
    position: absolute; right: 524px; top: 356px; text-align: right;
    list-style: none;
  }
  .resources-title {
    font-weight: 700; font-size: 21px; color: var(--brand-dark);
    margin-bottom: 8px;
  }
  .resources li { font-size: 18px; line-height: 30px; color: var(--ink); }

  .promo-box {
    position: absolute; left: 54px; top: 682px; width: 269px; height: 125px;
    background: var(--brand-bright); color: var(--paper);
    padding: 14px 0 0 12px;
  }
  .promo-headline { font-weight: 700; font-size: 32px; line-height: 1.05; }
  .promo-sub { font-weight: 400; font-size: 18px; line-height: 1.35; margin-top: 8px; letter-spacing: -0.4px; }

  .fruit-visual {
    position: absolute; left: 360px; top: 340px; width: 470px; height: 590px;
    border-radius: 24px;
    background: linear-gradient(180deg, var(--tone-green) 0%, var(--tone-yellow) 30%, var(--tone-orange) 52%, var(--tone-red) 72%, var(--tone-green) 100%);
  }

  .offer { position: absolute; left: 70px; top: 948px; }
  .offer-headline { font-weight: 300; font-size: 70px; line-height: 1; letter-spacing: -1px; color: var(--ink); }
  .offer-note { font-weight: 400; font-size: 21px; margin-top: 10px; color: var(--ink); }

  .contact-band {
    position: absolute; left: 0; top: 1069px; width: 847px; height: 131px;
    background: var(--footer-green); color: var(--paper);
    display: flex; flex-direction: column; align-items: center; justify-content: center;
    font-size: 21px; line-height: 1.5;
  }
</style>
</head>
<body>
<main class="leaflet">
  <div class="region-map" role="img" aria-label="Pale green regional map of Bedfordshire, Buckinghamshire, Milton Keynes and London areas"></div>

  <header class="brand">
    <div class="brand-row">
      <span class="brand-square"></span>
      <span class="brand-name">Oakridge</span>
    </div>
    <span class="brand-tagline">SALES &amp; LETTINGS</span>
  </header>

  <ul class="resources">
    <li class="resources-title">RESOURCES</li>
    <li>Property Management Explained</li>
    <li>Fees / Terms &amp; Conditions</li>
    <li>Step-By-Step Letting Guide</li>
    <li>FAQ For Landlords</li>
    <li>Energy Performance Certificates</li>
    <li>Safety Regulations</li>
    <li>Tenancy Deposits</li>
    <li>HomeKeep Service Comparison</li>
    <li>Foreign investors in the UK</li>
  </ul>

  <section class="promo-box">
    <p class="promo-headline">TAKE IT EASY</p>
    <p class="promo-sub">WE DO THE HARDWORK<br>SO YOU DON'T HAVE TO</p>
  </section>

  <div class="fruit-visual" role="img" aria-label="Photograph of fruit cut into stacked colourful slices with leaves"></div>

  <section class="offer">
    <p class="offer-headline">only 0.5% fee</p>
    <p class="offer-note">for instructions received in March 2015</p>
  </section>

  <footer class="contact-band">
    <p>info@oakridgehomes.co.uk &nbsp;|&nbsp; Call Us On 01632 960418</p>
    <p>www.oakridgehomes.co.uk</p>
  </footer>
</main>
</body>
</html>
```